Corvane Holdings , new business card design

investment firm with corporate clients . need double sided business card , vertical and horizontal options ,logo must be clear. prefer pantone colors only and sharp design. website also www.corvane-example.ae

Khalid Bin Rashed
Managing Director
Tel. +971 4 000 3829
Mobile +971 50 000 4172
khalid@corvane-example.ae
Palm Crest Tower, officw 18-B07, Qasr Gardens, Dubai

Contact Information for Business Card

Khalid Bin Rashed
Managing Director

Font styles to use
Serif

Colors

Designer to choose colors to be used in the design.

```html
<!DOCTYPE html>
<html lang="en">
<head>
<meta charset="utf-8">
<title>Corvane Holdings – Business Card</title>
<link href="https://fonts.googleapis.com/css2?family=Libre+Baskerville:wght@400;700&display=swap" rel="stylesheet">
<style>
  :root {
    --navy: #00205b;
    --blue: #0a8cff;
    --bar-blue: #0a66e0;
    --text-blue: #1a8cff;
    --slate: #807f84;
    --paper: #ffffff;
    --brand: #1f3f6e;
  }
  * { margin: 0; padding: 0; box-sizing: border-box; }
  html, body { width: 1200px; height: 686px; overflow: hidden; background: var(--paper); }
  .card {
    position: relative;
    width: 1200px;
    height: 686px;
    overflow: hidden;
    background: var(--paper);
    font-family: "Libre Baskerville", "Times New Roman", serif;
  }
  .card-shapes { position: absolute; inset: 0; }
  .brand {
    position: absolute;
    left: 72px;
    top: 286px;
    width: 436px;
    text-align: center;
    color: var(--brand);
    font-weight: 400;
    line-height: 1;
    white-space: nowrap;
  }
  .brand-name { font-size: 56px; letter-spacing: 14px; padding-left: 14px; }
  .brand-sub { font-size: 20px; letter-spacing: 21px; padding-left: 21px; margin-top: 20px; }
  .contact {
    position: absolute;
    right: 72px;
    text-align: right;
    color: var(--text-blue);
    font-weight: 700;
    font-size: 26px;
    line-height: 38px;
    white-space: nowrap;
  }
  .contact-name { top: 134px; }
  .contact-name .name { text-transform: uppercase; font-size: 27px; }
  .contact-name .role { font-size: 23px; line-height: 32px; }
  .contact-address { top: 250px; }
  .contact-phone { top: 372px; }
  .contact-email { top: 509px; }
</style>
</head>
<body>
<main class="card">
  <svg class="card-shapes" width="1200" height="686" viewBox="0 0 1200 686" aria-hidden="true">
    <defs>
      <linearGradient id="silver-fade" x1="0" y1="0" x2="1" y2="0">
        <stop offset="0" stop-color="#e2e3e5"/>
        <stop offset="1" stop-color="#c9cacd"/>
      </linearGradient>
    </defs>
    <rect class="edge-bar" x="0" y="105" width="41" height="476" fill="var(--navy)"/>
    <polygon class="silver-band" points="477,0 546,0 745,686 648,686" fill="url(#silver-fade)"/>
    <polygon class="slate-panel" points="546,0 1200,0 1200,686 745,686" fill="var(--slate)"/>

    <polygon class="tab tab-person" points="506,121 598,121 621,213 529,213" fill="var(--navy)"/>
    <polygon class="tab tab-address" points="536,242 633,242 656,333 559,333" fill="var(--blue)"/>
    <polygon class="tab tab-phone" points="566,362 659,362 682,453 589,453" fill="var(--blue)"/>
    <polygon class="tab tab-email" points="597,482 693,482 716,573 620,573" fill="var(--blue)"/>

    <g class="icon-person" fill="#ffffff">
      <circle cx="563" cy="157" r="9"/>
      <path d="M545 181 q2 -14 18 -14 q16 0 18 14 z"/>
    </g>
    <path class="icon-pin" d="M597 275 a11 11 0 0 1 11 11 c0 9 -11 21 -11 21 c0 0 -11 -12 -11 -21 a11 11 0 0 1 11 -11 z" fill="#ffffff"/>
    <circle cx="597" cy="286" r="4.5" fill="var(--blue)"/>
    <path class="icon-phone" d="M615 398 l6 -5 l6 8 l-4 4 q3 6 9 9 l4 -4 l8 6 l-5 6 q-14 0 -24 -24 z" fill="#ffffff"/>
    <rect class="icon-mail" x="642" y="517" width="30" height="22" fill="#ffffff"/>
    <path d="M644 519 l13 12 l13 -12 M644 537 l10 -9 M670 537 l-10 -9" stroke="var(--blue)" stroke-width="2" fill="none"/>

    <rect class="row-bar" x="1153" y="121" width="10" height="92" fill="var(--navy)"/>
    <rect class="row-bar" x="1153" y="242" width="10" height="91" fill="var(--bar-blue)"/>
    <rect class="row-bar" x="1153" y="362" width="10" height="91" fill="var(--bar-blue)"/>
    <rect class="row-bar" x="1153" y="482" width="10" height="91" fill="var(--bar-blue)"/>
  </svg>

  <div class="brand">
    <div class="brand-name">CORVANE</div>
    <div class="brand-sub">HOLDINGS</div>
  </div>

  <div class="contact contact-name">
    <div class="name">Khalid Bin Rashed</div>
    <div class="role">Managing Director</div>
  </div>
  <div class="contact contact-address">
    <div>Menara Palm Crest, Office 18-B07</div>
    <div>Qasr Gardens, Dubai</div>
  </div>
  <div class="contact contact-phone">
    <div>+971 4 000 3829</div>
    <div>+971 50 000 4172</div>
  </div>
  <div class="contact contact-email">
    <div>khalid@corvane-example.ae</div>
  </div>
</main>
</body>
</html>
```